Need Business Card for eLearning Company

Need a business card designed for our company, CareerPathlane.

CareerPathlane has developed a complete 12 lesson eLearning course to teach you the skills you need to present yourself in a job interview. The course uses advanced learning techniques in the multimedia videos, plus contains quizzes and additional exercises to insure you get the course and can walk into any interview with confidence and ease, and get the job.

www.careerpathlane-demo.com

Attached is our logo

Industry/Entity Type

Business

```html
<!DOCTYPE html>
<html lang="en">
<head>
<meta charset="utf-8">
<title>CareerPathlane Business Card</title>
<link href="https://fonts.googleapis.com/css2?family=Lato:wght@400;700&display=swap" rel="stylesheet">
<style>
  :root {
    --backdrop: #3b322d;
    --ink-dark: #333333;
    --ink-muted: #777777;
    --accent-green: #8cbf3f;
    --tile-light: #b8b8b8;
    --tile-mid: #8a8a8a;
    --tile-dark: #555555;
    --tile-darkest: #3e3e3e;
    --mark-square: #454545;
  }
  html, body {
    margin: 0;
    padding: 0;
    width: 1200px;
    height: 1000px;
    overflow: hidden;
    background: var(--backdrop);
    font-family: "Lato", Arial, sans-serif;
  }
  .canvas {
    position: relative;
    width: 1200px;
    height: 1000px;
  }
  .card {
    position: absolute;
    left: 300px;
    width: 600px;
    height: 340px;
    box-shadow: 0 10px 24px rgba(0,0,0,0.45);
  }
  .card-front { top: 90px; }
  .card-back { top: 550px; }
  .card svg { display: block; width: 600px; height: 340px; }
  .brand-name { font-family: "Lato", Arial, sans-serif; font-weight: 400; fill: var(--ink-dark); }
  .card-subline { font-family: "Lato", Arial, sans-serif; font-weight: 400; fill: var(--ink-muted); letter-spacing: 2px; }
  .web-address { font-family: "Lato", Arial, sans-serif; font-weight: 700; fill: var(--accent-green); letter-spacing: 6px; }
  .contact-line { font-family: "Lato", Arial, sans-serif; font-size: 15px; fill: var(--ink-muted); }
  .tile-person { fill: var(--tile-light); }
  .tile-mail { fill: var(--tile-dark); }
  .tile-phone { fill: var(--tile-darkest); }
  .tile-home { fill: var(--tile-mid); }
  .icon { fill: #ffffff; }
  .icon-line { stroke: var(--tile-dark); stroke-width: 1.6; fill: none; }
  .mark-square { fill: var(--mark-square); }
</style>
</head>
<body>
<main class="canvas">

  <section class="card card-front">
    <svg viewBox="0 0 600 340" xmlns="http://www.w3.org/2000/svg">
      <defs>
        <linearGradient id="cardSurfaceFront" x1="0" y1="0" x2="1" y2="1">
          <stop offset="0" stop-color="#ffffff"/>
          <stop offset="0.55" stop-color="#f3f3f3"/>
          <stop offset="1" stop-color="#e6e6e6"/>
        </linearGradient>
      </defs>
      <rect width="600" height="340" fill="url(#cardSurfaceFront)" role="img" aria-label="Light gray faceted diamond pattern background"/>
      <rect class="mark-square" x="82" y="140" width="50" height="50"/>
      <text class="brand-name" x="150" y="188" font-size="46">CareerPathlane</text>
      <text class="card-subline" x="152" y="218" font-size="13">INTERVIEW SKILLS ONLINE</text>
      <text class="web-address" x="300" y="322" font-size="12" text-anchor="middle">WWW.CAREERPATHLANE-DEMO.COM</text>
    </svg>
  </section>

  <section class="card card-back">
    <svg viewBox="0 0 600 340" xmlns="http://www.w3.org/2000/svg">
      <defs>
        <linearGradient id="cardSurfaceBack" x1="0" y1="0" x2="1" y2="1">
          <stop offset="0" stop-color="#ffffff"/>
          <stop offset="0.55" stop-color="#f3f3f3"/>
          <stop offset="1" stop-color="#e6e6e6"/>
        </linearGradient>
      </defs>
      <rect width="600" height="340" fill="url(#cardSurfaceBack)" role="img" aria-label="Light gray faceted diamond pattern background"/>

      <g class="brand-lockup">
        <rect class="mark-square" x="318" y="46" width="26" height="26"/>
        <text class="brand-name" x="352" y="70" font-size="26">CareerPathlane</text>
        <text class="card-subline" x="353" y="88" font-size="9">INTERVIEW SKILLS ONLINE</text>
      </g>

      <g class="contact-tiles">
        <rect class="tile-person" x="-30" y="-30" width="60" height="60" transform="translate(165 124) rotate(45)"/>
        <rect class="tile-mail" x="-30" y="-30" width="60" height="60" transform="translate(122 167) rotate(45)"/>
        <rect class="tile-phone" x="-30" y="-30" width="60" height="60" transform="translate(165 210) rotate(45)"/>
        <rect class="tile-home" x="-30" y="-30" width="60" height="60" transform="translate(122 253) rotate(45)"/>

        <g class="icon-person">
          <circle class="icon" cx="165" cy="117" r="8"/>
          <path class="icon" d="M151 137 Q151 125 165 125 Q179 125 179 137 Z"/>
        </g>
        <g class="icon-mail">
          <rect class="icon" x="109" y="158" width="26" height="18"/>
          <path class="icon-line" d="M109 158 L122 169 L135 158"/>
        </g>
        <g class="icon-phone">
          <path class="icon" d="M157 198 q4 -3 6 0 l3 5 q1 3 -2 4 q1 5 5 9 q2 -2 4 0 l4 4 q2 2 -1 5 q-3 3 -7 1 q-9 -5 -13 -16 q-2 -6 1 -12 z"/>
        </g>
        <g class="icon-home">
          <polygon class="icon" points="122,240 137,253 132,253 132,265 112,265 112,253 107,253"/>
        </g>
      </g>

      <g class="contact-details">
        <text class="contact-line" x="226" y="129">Your Name</text>
        <text class="contact-line" x="192" y="171">hello@careerpathlane-demo.com</text>
        <text class="contact-line" x="226" y="214">US:(555) 014-2286 / International:(55) 0100-3742</text>
        <text class="contact-line" x="192" y="257">420 Harbor View Road Suite 12, Lakeside, WA 90000</text>
      </g>
    </svg>
  </section>

</main>
</body>
</html>
```